Magazine advertisement

I need a company advertisement for magazine prints. I need to be able to scale it to different sizes if need be. I need it to showcase our brand, VornaDrive have our phone number 582.463.9047 our contact email address sales@vornadrive.net and web address www.vornadrive.net

Target Market(s)

automotive / tractor pulling

Industry/Entity Type

automotive / racing

Colors
EB3D1F
EC4F4E
F09395
F8D3D4
FCEDEE

Requirements
Must have
• our logo, our color scheme (pantone red 1795, white, black, silver

```html
<!DOCTYPE html>
<html lang="en">
<head>
<meta charset="utf-8">
<title>VornaDrive Magazine Advertisement</title>
<link rel="stylesheet" href="https://fonts.googleapis.com/css2?family=Montserrat:wght@400;500;700;800;900&display=swap">
<style>
  :root {
    --red: #d8202a;
    --red-deep: #8e0d14;
    --black: #111111;
    --charcoal: #1e1e1e;
    --paper: #f2f2f2;
    --white: #ffffff;
    --grey-text: #2a2a2a;
    --rule: #c9c9c9;
    --backdrop: #e4e5e8;
  }
  * { margin: 0; padding: 0; box-sizing: border-box; }
  html, body {
    width: 1200px; height: 1075px; overflow: hidden;
    background: var(--backdrop);
    font-family: "Montserrat", Arial, sans-serif;
  }
  .ad-page {
    position: absolute; left: 200px; top: 20px;
    width: 800px; height: 1035px;
    background: var(--paper);
    overflow: hidden;
    box-shadow: 0 6px 24px rgba(0,0,0,.15);
  }
  .hero-art { position: absolute; inset: 0; width: 800px; height: 1035px; }
  .brand-name {
    position: absolute; left: 0; right: 0; top: 50px;
    text-align: center; color: var(--white);
    font-weight: 900; font-size: 92px; line-height: 1; letter-spacing: 2px;
    text-transform: uppercase;
  }
  .headline {
    position: absolute; left: 48px; right: 40px; top: 718px;
    color: var(--red); font-weight: 800; font-size: 37px; line-height: 1.1; letter-spacing: -.5px;
    white-space: nowrap;
  }
  .info-columns {
    position: absolute; left: 48px; right: 40px; top: 778px;
    display: grid; grid-template-columns: repeat(3, 1fr);
  }
  .info-block { padding: 0 16px; border-left: 1px solid var(--rule); }
  .info-block:first-child { padding-left: 0; border-left: none; }
  .info-title { color: var(--red); font-weight: 800; font-size: 16px; line-height: 1.2; margin-bottom: 7px; }
  .info-text { color: var(--grey-text); font-size: 12px; line-height: 1.42; font-weight: 500; }
  .contact-bar {
    position: absolute; left: 0; right: 0; bottom: 0; height: 62px;
    background: var(--charcoal); color: var(--white);
    display: flex; align-items: center; justify-content: center; gap: 14px;
    font-size: 15px; font-weight: 400;
  }
  .contact-item { display: flex; align-items: center; gap: 7px; }
  .contact-social { margin-left: 18px; }
  .contact-divider { color: var(--red); }
  .contact-icon { width: 15px; height: 15px; }
  .social-dot { width: 12px; height: 12px; border-radius: 50%; background: var(--red); }
</style>
</head>
<body>
<main class="ad-page">
  <svg class="hero-art" viewBox="0 0 800 1035">
    <defs>
      <radialGradient id="heroGlow" cx="55%" cy="45%" r="70%">
        <stop offset="0" stop-color="#e0262e"/>
        <stop offset=".55" stop-color="#a3101a"/>
        <stop offset="1" stop-color="#3d0407"/>
      </radialGradient>
      <linearGradient id="turboMetal" x1="0" y1="0" x2="1" y2="1">
        <stop offset="0" stop-color="#e9e9ea"/>
        <stop offset="1" stop-color="#9a9a9d"/>
      </linearGradient>
    </defs>
    <rect x="0" y="0" width="800" height="640" fill="url(#heroGlow)" role="img" aria-label="Red automotive backdrop photograph"/>
    <g role="img" aria-label="Three polished turbochargers">
      <ellipse cx="170" cy="255" rx="85" ry="70" fill="url(#turboMetal)"/>
      <ellipse cx="400" cy="320" rx="85" ry="70" fill="url(#turboMetal)"/>
      <ellipse cx="630" cy="385" rx="85" ry="70" fill="url(#turboMetal)"/>
    </g>
    <polygon points="0,468 400,560 800,468 800,482 400,574 0,482" fill="var(--red)"/>
    <polygon points="0,482 400,574 800,482 800,700 0,700" fill="var(--black)"/>
    <polygon points="0,640 400,700 800,640 800,1035 0,1035" fill="var(--paper)"/>
    <polygon points="0,634 400,694 800,634 800,640 400,700 0,640" fill="var(--red)"/>
    <rect x="240" y="592" width="320" height="76" rx="4" fill="#2a2a2a" role="img" aria-label="Hand-lettered tagline: Built to Win"/>
  </svg>

  <div class="brand-name">VornaDrive</div>

  <h1 class="headline">The Most Advanced Turbine Wheel</h1>

  <section class="info-columns">
    <article class="info-block">
      <h2 class="info-title">What We Do</h2>
      <p class="info-text">We'll help you perform like a winner, from truck and tractor pulling to drag racing. Our turbochargers are equipped with the capacity to power everything from high-end sports cars to snowmobiles.</p>
    </article>
    <article class="info-block">
      <h2 class="info-title">Our History</h2>
      <p class="info-text">In 2019, we took the racing world by storm after unveiling our revolutionary turbocharger at the National Speed Parts Expo. During this event, our company set a new standard for turbocharged engines.</p>
    </article>
    <article class="info-block">
      <h2 class="info-title">Our Product</h2>
      <p class="info-text">Our team utilizes groundbreaking techniques to create upscale turbochargers that are guaranteed to defy your expectations. Our unique, patented wheel-design and advanced technology optimizes performance for a wide range of specialized vehicles.</p>
    </article>
  </section>

  <footer class="contact-bar">
    <span class="contact-item">
      <svg class="contact-icon" viewBox="0 0 16 16"><circle cx="8" cy="8" r="7" fill="none" stroke="var(--red)" stroke-width="1.6"/><path d="M5.5 4.5l1.5 1.5-1 1c.6 1.2 1.5 2.1 2.7 2.7l1-1 1.5 1.5-1 1.2C7.5 11 5 8.5 4.6 5.6z" fill="var(--red)"/></svg>
      582.463.9047
    </span>
    <span class="contact-divider">/</span>
    <span class="contact-item">
      <svg class="contact-icon" viewBox="0 0 16 16"><rect x="1.5" y="3.5" width="13" height="9" fill="none" stroke="var(--red)" stroke-width="1.4"/><path d="M1.5 3.5l6.5 5 6.5-5" fill="none" stroke="var(--red)" stroke-width="1.4"/></svg>
      sales@vornadrive.net
    </span>
    <span class="contact-divider">/</span>
    <span class="contact-item">
      <svg class="contact-icon" viewBox="0 0 16 16"><circle cx="8" cy="8" r="6.5" fill="none" stroke="var(--red)" stroke-width="1.4"/><ellipse cx="8" cy="8" rx="3" ry="6.5" fill="none" stroke="var(--red)" stroke-width="1.2"/><path d="M1.5 8h13" stroke="var(--red)" stroke-width="1.2"/></svg>
      www.vornadrive.net
    </span>
    <span class="contact-item contact-social">
      <span class="social-dot"></span>
      VornaDrive
    </span>
  </footer>
</main>
</body>
</html>
```